Business card for marketing analytics company

Need a business card for new company. I have a logo already that I want to be built into the card and should use those colours

Company is called Ostara Metrics
Design must bring Ostara Metrics to life not be a card that could be for anyone with a logo put on it.

Like the front to be fairly clean and uncluttered bringing the logo out with a suitable design on the back of the card.

The logo represents a compass and business growth so those themes along with numbers, analytics , data are appropriate.
I'm often working with creative industries so also needs to reflect the creative side of analytics rather than be very corporate looking.

Target Market(s)

Ad agency, media agency, consumer goods clients

Industry/Entity Type

Market Research

Contact Information for Business Card

Needs to include name, title, email and phone number

Colors
f78f20
f68d4d
ec1f27

Requirements
Must have
• Must bring Ostara Metrics to life not be a card that could be for anyone with a logo put on it.
• Logo, Correct colours
• Like a design on the back that relates to company name
• Designs for both sides
Should not have
• Please do not just submit logo and a coloured card.
• It needs to have a design element to it
• No black background
• No clear cards - needs front & back

```html
<!DOCTYPE html>
<html lang="en">
<head>
<meta charset="utf-8">
<title>Ostara Metrics business card</title>
<link rel="stylesheet" href="https://fonts.googleapis.com/css2?family=Nunito:wght@700&family=Questrial&display=swap">
<style>
  :root {
    --slate: #4a5a62;
    --orange: #f78f20;
    --bright-orange: #f26a1b;
    --coral: #f68d4d;
    --red: #ec1f27;
    --deep-red: #c8202a;
    --paper: #f7f7f5;
    --backdrop: #e9e7e4;
    --ink: #4a5a62;
  }
  html, body {
    margin: 0;
    width: 1200px;
    height: 872px;
    overflow: hidden;
    background: var(--backdrop);
  }
  .canvas {
    width: 1200px;
    height: 872px;
    display: flex;
    align-items: center;
    justify-content: center;
    gap: 40px;
  }
  .card {
    position: relative;
    width: 540px;
    height: 310px;
    background: var(--paper);
    overflow: hidden;
    box-shadow: 0 6px 18px rgba(0,0,0,0.18);
  }
  .card-bands {
    position: absolute;
    inset: 0;
  }
  .band-slate { fill: var(--slate); }
  .band-orange { fill: var(--bright-orange); }
  .band-red { fill: var(--deep-red); }
  .card-field { fill: var(--paper); }

  /* front */
  .front-mark {
    position: absolute;
    left: 150px;
    top: 46px;
    display: flex;
    align-items: center;
    gap: 12px;
  }
  .mark-dot {
    width: 26px;
    height: 26px;
    border-radius: 50%;
    background: var(--coral);
    flex: none;
  }
  .front-mark .company-name {
    font-family: "Nunito", sans-serif;
    font-weight: 700;
    font-size: 30px;
    color: var(--coral);
    letter-spacing: 0.5px;
  }
  .person {
    position: absolute;
    left: 250px;
    top: 150px;
  }
  .person-name {
    margin: 0;
    font-family: "Questrial", sans-serif;
    font-weight: 400;
    font-size: 34px;
    line-height: 1;
    color: var(--ink);
    letter-spacing: 0.5px;
  }
  .person-title {
    margin: 6px 0 0;
    font-family: "Questrial", sans-serif;
    font-size: 12px;
    color: var(--red);
    letter-spacing: 1px;
  }
  .contact-list {
    list-style: none;
    margin: 14px 0 0 -28px;
    padding: 0;
    font-family: "Questrial", sans-serif;
    font-size: 12px;
    color: var(--ink);
  }
  .contact-list li {
    display: flex;
    align-items: center;
    gap: 8px;
    margin-bottom: 7px;
  }
  .contact-icon { width: 14px; height: 14px; flex: none; }

  /* back */
  .back-mark {
    position: absolute;
    inset: 0;
    display: flex;
    align-items: center;
    justify-content: center;
    gap: 14px;
  }
  .back-mark .mark-dot {
    width: 34px;
    height: 34px;
    background: var(--orange);
  }
  .back-mark .company-name {
    font-family: "Nunito", sans-serif;
    font-weight: 700;
    font-size: 36px;
    color: var(--slate);
  }
</style>
</head>
<body>
<main class="canvas">

  <section class="card card-front" aria-label="Card front">
    <svg class="card-bands" viewBox="0 0 540 310" aria-hidden="true">
      <rect class="band-slate" width="540" height="310"/>
      <polygon class="band-orange" points="112,0 540,0 540,310 112,310 44,155"/>
      <polygon class="band-red" points="138,0 540,0 540,310 138,310 70,155"/>
      <polygon class="card-field" points="152,0 540,0 540,310 152,310 84,155"/>
    </svg>
    <div class="front-mark">
      <span class="mark-dot"></span>
      <span class="company-name">Ostara Metrics</span>
    </div>
    <div class="person">
      <h1 class="person-name">YOUR NAME</h1>
      <p class="person-title">TITLE</p>
      <ul class="contact-list">
        <li>
          <svg class="contact-icon" viewBox="0 0 14 14" aria-hidden="true">
            <circle cx="7" cy="7" r="7" fill="var(--red)"/>
            <path d="M4.6 3.6c.4-.3.9-.2 1.1.2l.6 1.1c.2.4.1.8-.2 1l-.4.3c.3.8.9 1.5 1.7 1.9l.3-.4c.3-.3.7-.4 1-.2l1.1.6c.4.2.5.7.2 1.1l-.5.6c-.4.4-1 .5-1.6.3C6 9.4 4.6 8 3.9 6.2c-.2-.6-.1-1.2.3-1.6z" fill="#fff"/>
          </svg>
          <span>+0000 000 000</span>
        </li>
        <li>
          <svg class="contact-icon" viewBox="0 0 14 14" aria-hidden="true">
            <circle cx="7" cy="7" r="7" fill="var(--orange)"/>
            <rect x="3.5" y="4.5" width="7" height="5" rx="0.6" fill="#fff"/>
            <path d="M3.8 4.9 7 7.4l3.2-2.5" fill="none" stroke="var(--orange)" stroke-width="0.8"/>
          </svg>
          <span>hello@ostarametrics.com</span>
        </li>
      </ul>
    </div>
  </section>

  <section class="card card-back" aria-label="Card back">
    <svg class="card-bands" viewBox="0 0 540 310" aria-hidden="true">
      <rect class="band-slate" width="540" height="310"/>
      <polygon class="band-orange" points="112,0 428,0 496,155 428,310 112,310 44,155"/>
      <polygon class="band-red" points="138,0 402,0 470,155 402,310 138,310 70,155"/>
      <polygon class="card-field" points="152,0 388,0 456,155 388,310 152,310 84,155"/>
    </svg>
    <div class="back-mark">
      <span class="mark-dot"></span>
      <span class="company-name">Ostara Metrics</span>
    </div>
  </section>

</main>
</body>
</html>
```